Design the Keystone HR business card for my new business

I've just had a logo designed (attached) for my new business doing HR consulting. I'm a one person operation at this stage, my aim is to provide support and help to small to medium sized businesses with their people objectives or issues.

I'm not really into anything overly flashy, I'm not a PR or marketing agency. I'd like my card to look modern, professional and not gimmicky.

I'm thinking black front (to go with logo), double sided with details on the back, maybe in a different colour?

Logo attached in several different formats.

Front of the card to have logo and added text: People and Development Solutions

Back of the card to also feature logo in some way and say:
Megan Tulloch
PO Box (TBA)
Marrowvale QLD 4391
0438 512 976
megan@keystonehr.com.au
www.keystonehr.com.au

Target Market(s)

Small to medium businesses / business owners.

Industry/Entity Type

Marketing

Requirements
Must have
• Double sided business card.
Should not have
• Anything overly gimmicky.

```html
<!DOCTYPE html>
<html lang="en">
<head>
<meta charset="utf-8">
<title>Keystone HR – Business Card</title>
<link rel="stylesheet" href="https://fonts.googleapis.com/css2?family=Questrial&display=swap">
<style>
  :root {
    --backdrop: #d6d6d6;
    --card: #000000;
    --ink: #ffffff;
    --violet: #9b3fd1;
    --violet-soft: #3a1150;
    --rule: #2c2c2c;
  }
  * { margin: 0; padding: 0; box-sizing: border-box; }
  html, body {
    width: 1200px;
    height: 900px;
    overflow: hidden;
    background: var(--backdrop);
  }
  .canvas {
    position: relative;
    width: 1200px;
    height: 900px;
    font-family: "Questrial", "Century Gothic", sans-serif;
    color: var(--ink);
  }
  .card {
    position: absolute;
    background: var(--card);
    overflow: hidden;
  }

  /* Front */
  .card--front {
    left: 56px;
    top: 40px;
    width: 678px;
    height: 484px;
  }
  .brand {
    position: absolute;
    display: flex;
    align-items: center;
  }
  .brand__dot {
    flex: none;
    border-radius: 50%;
    border: 3px solid var(--violet);
  }
  .brand__name {
    font-weight: 400;
    color: var(--ink);
    white-space: nowrap;
    line-height: 1;
  }
  .card--front .brand {
    left: 70px;
    top: 180px;
  }
  .card--front .brand__dot {
    width: 150px;
    height: 150px;
    margin-right: 40px;
  }
  .card--front .brand__name {
    font-size: 64px;
  }
  .tagline {
    position: absolute;
    left: 262px;
    top: 300px;
    font-size: 15px;
    letter-spacing: 0.2px;
  }

  /* Back */
  .card--back {
    left: 440px;
    top: 396px;
    width: 700px;
    height: 464px;
  }
  .card--back .brand {
    right: 62px;
    top: 80px;
  }
  .card--back .brand__dot {
    width: 60px;
    height: 60px;
    border-width: 2px;
    margin-right: 14px;
  }
  .card--back .brand__name {
    font-size: 34px;
  }
  .divider {
    position: absolute;
    left: 656px;
    top: 24px;
    width: 1px;
    height: 160px;
    background: var(--rule);
  }
  .accent-circle {
    position: absolute;
    left: -40px;
    top: 170px;
    width: 300px;
    height: 300px;
    border-radius: 50%;
    background: radial-gradient(circle, var(--violet-soft) 0%, #1a0724 70%);
  }
  .contact {
    position: absolute;
    right: 58px;
    top: 256px;
    font-style: normal;
    text-align: right;
    font-size: 20px;
    line-height: 27px;
  }
</style>
</head>
<body>
<main class="canvas">
  <section class="card card--front" aria-label="Card front">
    <div class="brand">
      <span class="brand__dot"></span>
      <span class="brand__name">Keystone HR</span>
    </div>
    <p class="tagline">People and Development Solutions</p>
  </section>

  <section class="card card--back" aria-label="Card back">
    <div class="accent-circle" aria-hidden="true"></div>
    <div class="brand">
      <span class="brand__dot"></span>
      <span class="brand__name">Keystone HR</span>
    </div>
    <div class="divider" aria-hidden="true"></div>
    <address class="contact">
      Megan Tulloch<br>
      PO Box (TBA)<br>
      Marrowvale QLD 4391<br>
      0438 512 976<br>
      megan@keystonehr.com.au<br>
      www.keystonehr.com.au
    </address>
  </section>
</main>
</body>
</html>
```